Capability Statement Document/Flyer

Take the existing words from the capability statement document (attached) and design a unique folder/flyer document for professional use. Maybe something like a trifold or bifold style. Use approved colours and logo as per the attached files.
Our company designs and builds small onshore gas processing plants.

```html
<!DOCTYPE html>
<html lang="en">
<head>
<meta charset="utf-8">
<title>Veridan Capability Statement</title>
<link rel="stylesheet" href="https://fonts.googleapis.com/css2?family=Montserrat:ital,wght@0,400;0,500;0,600;0,700;0,800;1,500;1,600;1,700&display=swap">
<style>
:root{
  --green:#0b7a66;
  --grey:#c4c4c4;
  --grey-bg:#e0e0e0;
  --ink:#333333;
  --white:#ffffff;
}
*{margin:0;padding:0;box-sizing:border-box}
html,body{width:849px;height:1200px;overflow:hidden}
body{background:var(--grey-bg);font-family:'Montserrat',sans-serif;color:var(--ink);position:relative}
.page{position:absolute;left:34px;width:780px;height:551px;background:var(--white);border:1px solid #333;overflow:hidden}
.page--front{top:29px}
.page--inside{top:620px}
.deco{position:absolute;left:0;top:0;width:780px;height:551px;pointer-events:none}
.abs{position:absolute}
.green{color:var(--green)}

/* headings */
.section-title{font-weight:800;color:var(--green);text-align:center;line-height:1.1}

/* personnel */
.staff{position:absolute;width:163px;font-size:6.4px;line-height:7.9px}
.staff-bar{height:11.5px;background:var(--green);color:var(--white);font-weight:600;font-size:6.4px;line-height:11.5px;padding-left:4px;margin-bottom:4px;white-space:nowrap;
  clip-path:polygon(0 0,100% 0,100% 70%,calc(100% - 4px) 100%,4px 100%,0 70%)}
.staff p{margin-bottom:7.5px;text-align:justify}
.staff .exp{margin-bottom:8px}

/* brand words */
.brand{font-weight:700;color:var(--green);letter-spacing:1px;line-height:1}

/* contact */
.contact-row{position:absolute;left:205px;display:flex;align-items:center;font-size:6.8px}
.contact-icon{width:19px;height:19px;background:var(--green);display:flex;align-items:center;justify-content:center;margin-right:4px}
.divider{position:absolute;left:195px;top:397px;width:1px;height:95px;background:var(--grey)}

/* photo */
.photo{position:absolute;left:390px;top:146px;width:390px;height:209px;
  background:linear-gradient(180deg,#7fb6e6 0%,#b9d6ee 38%,#d9d3c4 55%,#c99a62 75%,#b88a58 100%)}
.photo-base{position:absolute;left:390px;top:355px;width:390px;height:7px;background:var(--grey)}

/* pills */
.pill{position:absolute;background:var(--green);color:var(--white);font-weight:700;text-align:center;
  clip-path:polygon(0 0,100% 0,100% 65%,calc(100% - 5px) 100%,0 100%,0 35%,5px 0)}
.pill--left{text-align:left;padding-left:5px}

.para{position:absolute;text-align:center;font-size:6.8px;line-height:9.1px}
.para b{color:var(--green);font-style:italic;font-weight:700}

.principles{position:absolute;left:68px;top:326px;list-style:none;font-size:6.5px;line-height:8px;font-weight:700;font-style:italic;color:var(--green)}
.principles li{display:flex;margin-bottom:5px}
.principles span{width:15px;flex:none}

/* tables */
.grid{position:absolute;border-collapse:collapse;table-layout:fixed;font-size:5.2px;line-height:6.3px;text-align:center}
.grid th{background:var(--green);color:var(--white);font-size:8px;font-weight:700;height:13.5px;border:0.5px solid var(--white)}
.grid td{border:0.5px solid #9a9a9a;padding:0 2px}
.grid td.fn{color:var(--green);font-weight:700;font-size:5.4px}
.grid td.num{color:var(--green);font-weight:700}

.list{position:absolute;left:592px;width:170px;list-style:none;font-size:6.8px;line-height:8.5px}
.list li{display:flex;margin-bottom:8.5px}
.list .mark{width:8px;flex:none;color:var(--green);font-weight:700}
</style>
</head>
<body>

<!-- FRONT SPREAD -->
<section class="page page--front">
  <svg class="deco" viewBox="0 0 1493 1054" preserveAspectRatio="none">
    <polygon points="0,0 256,0 256,93 0,158" fill="var(--green)"/>
    <polygon points="0,102 440,0 470,0 0,118" fill="var(--grey)"/>
    <rect x="0" y="1022" width="1300" height="32" fill="var(--grey)"/>
    <polygon points="1296,990 1493,938 1493,1054 1296,1054" fill="var(--green)"/>
    <polygon points="1296,1030 1493,980 1493,994 1296,1044" fill="var(--grey)"/>
  </svg>

  <h2 class="section-title abs" style="left:95px;top:97px;width:200px;font-size:13.6px">Key<br>Veridan Personnel</h2>
  <div class="abs green" style="left:95px;top:133px;width:200px;text-align:center;font-size:6.4px;font-weight:700;font-style:italic">KEY VERIDAN PERSONNEL</div>

  <div class="staff" style="left:22px;top:149px">
    <div class="staff-bar">Name:&nbsp;&nbsp; Liam Barrett&nbsp;&nbsp;&nbsp; Role:&nbsp;&nbsp; Executive Director</div>
    <p class="exp">35yrs Exp: Harbor Petroleum, Northcape Energy, Redline Gas, Eastmark Energy</p>
    <p>Extensive global energy industry experience, from frontline O&amp;M to the boardroom.</p>
    <p>Respected ‘C Suite’ leader with a track record of building high performing teams that deliver outstanding results.</p>
  </div>
  <div class="staff" style="left:205px;top:149px">
    <div class="staff-bar">Name:&nbsp; Dean Hollis&nbsp;&nbsp;&nbsp; Role:&nbsp; Commercial Director</div>
    <p class="exp">40yrs Exp: Coralbay Resources, Tidewater LNG, Meridian Oil, Redline Gas</p>
    <p>Senior Logistics &amp; Supply Chain Manager / Procurement Manager with strong operational, commercial, project management, negotiating &amp; relationship building skills. Experienced in operating complex and diverse logistics operations, significantly improving service levels whilst reducing cost.</p>
  </div>
  <div class="staff" style="left:22px;top:244px;line-height:9.1px">
    <div class="staff-bar">Name:&nbsp;&nbsp; Neil Ashford Role:&nbsp;&nbsp; Technical Director</div>
    <p class="exp">39yrs Exp: Harbor Petroleum, Northcape Energy, Gulf Petroleum Development, Meridian Oil, Kestrel Group, Basin Gas Co, Redline Gas, Eastmark Energy</p>
    <p>Highly skilled &amp; experienced operations &amp; project management professional with 39 years’ experience in the global oil &amp; gas industry delivering multiple projects and establishing best in class operational assets. Deep knowledge of project management, construction, commissioning &amp; start-up including a global functional assurance role.</p>
  </div>
  <div class="staff" style="left:205px;top:244px;line-height:9.1px">
    <div class="staff-bar">Name: Paul Rennick&nbsp; Role:&nbsp; Operations Director</div>
    <p class="exp">27yrs Exp: Meridian Oil, Kestrel Group, Basin Gas Co, Redline Gas, Eastmark Energy</p>
    <p>27 years’ success leading operations, maintenance and commissioning teams on onshore and offshore oil and gas production platforms, FPSOs, gas processing, coal seam gas, refrigeration facilities, and chemical refineries. Results driven and enthusiastic Leader with a proven track record of delivery.</p>
  </div>

  <div class="brand abs" style="left:470px;top:84px;width:230px;text-align:center;font-size:40px">VERIDAN</div>

  <div class="photo" role="img" aria-label="Photograph of an onshore gas processing plant with pipework and workers under a blue sky"></div>
  <div class="photo-base"></div>

  <div class="brand abs" style="left:72px;top:428px;width:112px;text-align:center;font-size:18px">VERIDAN</div>
  <div class="divider"></div>

  <div class="contact-row" style="top:396px">
    <div class="contact-icon"><svg width="10" height="11" viewBox="0 0 10 11"><path d="M5 0.5a3.6 3.6 0 0 0-3.6 3.6C1.4 6.8 5 10.5 5 10.5s3.6-3.7 3.6-6.4A3.6 3.6 0 0 0 5 .5z" fill="#fff"/><circle cx="5" cy="4.1" r="1.4" fill="var(--green)"/></svg></div>
    123 Dummy, Lorem Ipsum
  </div>
  <div class="contact-row" style="top:422px">
    <div class="contact-icon"><svg width="10" height="10" viewBox="0 0 10 10"><path d="M2 0.6 3.6 0.3 4.5 2.8 3.3 3.8c.6 1.3 1.6 2.3 2.9 2.9l1-1.2 2.5.9-.3 1.6C8.8 8.9 8 9.5 7 9.4 3.5 9 1 6.5.6 3 .5 2 1.1 1.2 2 .6z" fill="#fff"/></svg></div>
    +00 1234 5XXX 9012
  </div>
  <div class="contact-row" style="top:448px">
    <div class="contact-icon"><svg width="11" height="8" viewBox="0 0 11 8"><rect x=".5" y=".5" width="10" height="7" fill="none" stroke="#fff"/><path d="M.5 .5 5.5 4.5 10.5 .5M.5 7.5 4 3.8M10.5 7.5 7 3.8" fill="none" stroke="#fff" stroke-width=".8"/></svg></div>
    Your eamil space
  </div>
  <div class="contact-row" style="top:474px">
    <div class="contact-icon"><svg width="8" height="11" viewBox="0 0 8 11"><path d="M1 .5v8.5l2.2-2 1.5 3.5 1.4-.6-1.5-3.4H7.5z" fill="#fff"/></svg></div>
    website address here
  </div>

  <h1 class="abs" style="left:430px;top:399px;width:310px;text-align:center;font-size:20px;font-weight:800;color:var(--green);letter-spacing:.6px">CAPABILITY STATEMENT</h1>
  <div class="abs" style="left:430px;top:425px;width:310px;text-align:center;font-size:9px;font-weight:700;font-style:italic">Simplify Project Execution, Streamline Operations</div>
</section>

<!-- INSIDE SPREAD -->
<section class="page page--inside">
  <svg class="deco" viewBox="0 0 1493 1054" preserveAspectRatio="none">
    <polygon points="0,0 256,0 256,93 0,158" fill="var(--green)"/>
    <polygon points="0,102 440,0 470,0 0,118" fill="var(--grey)"/>
    <rect x="0" y="1022" width="1300" height="32" fill="var(--grey)"/>
    <polygon points="1296,990 1493,938 1493,1054 1296,1054" fill="var(--green)"/>
    <polygon points="1296,1030 1493,980 1493,994 1296,1044" fill="var(--grey)"/>
  </svg>

  <h2 class="section-title abs" style="left:65px;top:99px;width:261px;font-size:14.6px">Who are Veridan?</h2>
  <p class="para" style="left:62px;top:123px;width:267px"><b>Veridan</b> are a highly experienced team of Executive, Project, Construction, Commissioning and Operations specialists who combine deep technical knowledge with proven leadership to deliver unique <b>Project Delivery Partner</b> services to organisations in Australia.</p>

  <div class="pill" style="left:118px;top:175px;width:156px;height:14.6px;font-size:9px;line-height:14.6px">Our vision is straightforward:</div>
  <div class="abs green" style="left:80px;top:194px;width:230px;text-align:center;font-size:6.5px;font-weight:700;font-style:italic">Simplify Project Execution, Streamline Operations.</div>

  <h2 class="section-title abs" style="left:40px;top:211px;width:311px;font-size:13.8px">What is a Project Delivery Partner?</h2>
  <p class="para" style="left:65px;top:238px;width:261px">A Project Delivery Partner (PDP) provides integrated project management along with technical, commercial and delivery support services to help an organisation successfully deliver a project. The PDP acts as the owner’s team while the owner retains accountability and key decision-making authority.</p>

  <div class="pill pill--left" style="left:68px;top:313px;width:114px;height:11.5px;font-size:6.4px;font-weight:600;line-height:11.5px">PDP Core Principles:</div>
  <ul class="principles">
    <li><span>1.</span>Owner controls the project</li>
    <li><span>2.</span>PDP enables delivery &amp;<br>provides assurance</li>
    <li><span>3.</span>Contractors execute<br>the work</li>
  </ul>

  <svg class="deco" viewBox="0 0 780 551">
    <g fill="var(--green)">
      <polygon points="201,312 244,312 250,318 250,345 207,345 201,339"/>
      <polygon points="201,358 244,358 250,364 250,392 207,392 201,386"/>
      <polygon points="129,404 172,404 178,410 178,438 135,438 129,432"/>
      <polygon points="201,404 244,404 250,410 250,438 207,438 201,432"/>
      <polygon points="272,404 315,404 321,410 321,438 278,438 272,432"/>
    </g>
    <g stroke="var(--green)" stroke-width=".6" fill="none">
      <line x1="225.5" y1="345" x2="225.5" y2="358"/>
      <line x1="225.5" y1="392" x2="225.5" y2="404"/>
      <polyline points="153.5,404 153.5,398.5 296.5,398.5 296.5,404"/>
    </g>
    <g font-family="Montserrat, sans-serif" font-size="6.6" font-weight="500" fill="#fff" text-anchor="middle">
      <text x="225.5" y="326">OPERATOR</text>
      <text x="225.5" y="335">XYZ</text>
      <text x="225.5" y="377.5">VERIDAN</text>
      <text x="153.5" y="423.5">VERIDAN</text>
      <text x="225.5" y="423.5">VERIDAN</text>
      <text x="296.5" y="423.5">VERIDAN</text>
    </g>
    <g font-family="Montserrat, sans-serif" font-size="6.5" font-weight="700" font-style="italic" fill="var(--green)">
      <text x="225.5" y="305" text-anchor="middle">OWNER</text>
      <text x="258" y="367">PROJECT</text>
      <text x="258" y="376">DELIVERY</text>
      <text x="258" y="385">PARTNER</text>
      <text x="68" y="424">CONTRACTORS</text>
    </g>
  </svg>

  <h3 class="abs green" style="left:129px;top:445px;font-size:9px;font-weight:800">PDP Objective:</h3>
  <p class="abs" style="left:129px;top:463px;width:200px;font-size:6.8px;line-height:9.1px">Deliver the project safely, on schedule, within budget and ready for operations; providing owner capability throughout the project lifecycle.</p>

  <h2 class="section-title abs" style="left:434px;top:42px;width:120px;font-size:13.6px">PDP<br>Services:</h2>
  <table class="grid" style="left:414px;top:80px;width:160px">
    <colgroup><col style="width:14.6px"><col style="width:67px"><col></colgroup>
    <tr><th>#</th><th>Function</th><th>Veridan Service</th></tr>
    <tr style="height:25px"><td class="num">1</td><td class="fn">Project Management</td><td>Planning, Reporting &amp; Delivery Leadership from Concept to Completion</td></tr>
    <tr style="height:31.4px"><td class="num">2</td><td class="fn">Engineering</td><td>Concept Selection, Design Coordination, Technical Assurance &amp; Value Engineering</td></tr>
    <tr style="height:25px"><td class="num">3</td><td class="fn">Procurement</td><td>Contracting Strategy, Tender Process &amp; Supplier/ Contractor Management</td></tr>
    <tr style="height:25px"><td class="num">4</td><td class="fn">Approvals</td><td>Land Access, Regulator Engagement, Safety Case, Permits &amp; Licenses</td></tr>
    <tr style="height:31.4px"><td class="num">5</td><td class="fn">Cost Control</td><td>Budget Development, Forecasting &amp; Management</td></tr>
    <tr style="height:31.4px"><td class="num">6</td><td class="fn">Scheduling</td><td>Master Schedule Development, WBS, Resource Allocation, Monitoring &amp; Updating</td></tr>
    <tr style="height:30.3px"><td class="num">7</td><td class="fn">Risk Management</td><td>Risk Register, Identification, Mitigation &amp; Reporting</td></tr>
    <tr style="height:31.4px"><td class="num">8</td><td class="fn">Governance</td><td>Framework, Stage Gates, Change control, Reporting &amp; Decision Support</td></tr>
    <tr style="height:31.4px"><td class="num">9</td><td class="fn">Construction</td><td>Management &amp; Coordination of Contractor Execution Teams</td></tr>
    <tr style="height:31.4px"><td class="num">10</td><td class="fn">Commissioning &amp;<br>Start-up</td><td>Lead Commissioning &amp; Start-up, Completions System, Bring the Facility to Steady-State</td></tr>
    <tr style="height:31.4px"><td class="num">11</td><td class="fn">Operations<br>Readiness</td><td>People &amp; Organisation, Process &amp; Procedures, Systems &amp; Technology</td></tr>
    <tr style="height:31.4px"><td class="num">12</td><td class="fn">Operations &amp;<br>Maintenance</td><td>Monitor &amp; Operate Asset, Minimize Downtime, Lowest Possible OPEX for Owner</td></tr>
  </table>

  <div class="pill" style="left:414px;top:468px;width:162px;height:19.5px;font-size:6.6px;line-height:8px;padding-top:2px"><i>For More Information Contact:</i><br>directors@veridan.com.au</div>

  <h2 class="section-title abs" style="left:596px;top:42px;width:160px;font-size:13.6px">PDP Roles &amp;<br>Responsibilities:</h2>
  <table class="grid" style="left:595px;top:80px;width:163px">
    <colgroup><col style="width:81.5px"><col></colgroup>
    <tr><th>Owner</th><th>Veridan Service</th></tr>
    <tr style="height:21.4px"><td class="fn">Sets Project Objectives</td><td>Develops<br>Delivery Plans</td></tr>
    <tr style="height:20.9px"><td class="fn">Approves Major Decisions</td><td>Provides<br>Recommendations</td></tr>
    <tr style="height:20.9px"><td class="fn">Holds Project Risk</td><td>Identifies and<br>Manages Risks</td></tr>
    <tr style="height:20.4px"><td class="fn">Awards Contracts</td><td>Manages Contractor<br>Interfaces</td></tr>
    <tr style="height:31.9px"><td class="fn">Provides Funding</td><td>Monitors Cost and<br>Schedule Performance</td></tr>
  </table>

  <div class="pill pill--left" style="left:592px;top:224px;width:80px;height:14.6px;font-size:9px;line-height:14.6px">PDP Benefits:</div>
  <ul class="list" style="top:242px">
    <li><span class="mark">✔</span>Provides owners with access to experienced project delivery capability</li>
    <li><span class="mark">✔</span>Improved project controls and governance</li>
    <li><span class="mark">✔</span>Greater flexibility than traditional EPC delivery</li>
    <li><span class="mark">✔</span>Enhanced visibility and management of cost, schedule and risk</li>
    <li><span class="mark">✔</span>Scalable resources aligned with project phases</li>
  </ul>

  <div class="pill pill--left" style="left:592px;top:349px;width:93px;height:14.6px;font-size:9px;line-height:14.6px">PDP Challenges:</div>
  <ul class="list" style="top:366px">
    <li><span class="mark">✘</span>Owner retains significant delivery risk</li>
    <li><span class="mark">✘</span>Requires clear governance and decision-making processes</li>
    <li><span class="mark">✘</span>Multiple contractor interfaces require strong coordination</li>
    <li><span class="mark">✘</span>Success depends on collaborative Owner-PDP relationship</li>
  </ul>
</section>

</body>
</html>
```